Cobalt MesaLighting and Design Web Page

We are a Sales Agency that represents 40+ LED Lighting manufacturers primarily in new commercial, industrial and architectural construction projects. We also are active in the Re-Light and Retrofit Lighting market.
Our current web page can be found at www.cobaltmesalighting.example. Our local competitors are www.brightfieldlampsnw.example,. We would like a more dynamic website that will list our manufacturers we represent and links to their websites. Please offer suggestions to provide a more dynamic website using our new logo which is attached. Please use the color scheme from logo. The final design should communicate innovation and expertise in LED lighting.

Target Market(s)

Architects, Lighting designers, Electrical Engineers, Electrical Contractors, Electrical Distributors, Facility Engineers, Energy Engineers

Industry/Entity Type

Construction

Number of Pages Required

5+ page

Font styles to use
Other font styles liked:
• MS Reference Sans Serif, or close to our LOGO font.

Colors
f78f20
959595

Requirements
Must have
• Logo incorporated with matching background, clean professional look based on logo, links to our manufacturers web page
Nice to have
• LED Lighting project stock photos as examples
Should not have
• crowded pages with text

```html
<!DOCTYPE html>
<html lang="en">
<head>
<meta charset="utf-8">
<title>Cobalt Mesa Lighting and Design</title>
<link rel="stylesheet" href="https://fonts.googleapis.com/css2?family=Orbitron:wght@500;700&family=Open+Sans:wght@400;600;700&display=swap">
<style>
:root{
  --orange:#f78f20;
  --grey:#959595;
  --dark:#2f2f2f;
  --darker:#1c1c1c;
  --band:#3e3e3e;
  --panel:#efefef;
  --text:#333;
  --muted:#c4c4c4;
}
*{box-sizing:border-box;margin:0;padding:0}
html,body{width:1200px;height:4380px;overflow:hidden}
body{position:relative;background:#fff;font-family:"Open Sans",Arial,sans-serif;color:var(--text)}
.abs{position:absolute}
.photo{position:absolute}

/* header */
.site-header{position:absolute;left:0;top:0;width:1200px;height:82px}
.nav-link{position:absolute;top:30px;font-size:13px;color:var(--orange);letter-spacing:1px;text-transform:uppercase;display:flex;align-items:center;gap:7px}
.nav-menu{left:30px}
.nav-follow{right:30px}
.brand{position:absolute;left:50%;top:14px;transform:translateX(-50%);display:flex;align-items:center;gap:10px}
.brand-mark{width:40px;height:40px;border:2px solid var(--orange);border-radius:50%}
.brand-name{font-size:13px;line-height:16px;font-weight:600;color:var(--orange);text-transform:uppercase;letter-spacing:1px}

/* cards */
.card{position:absolute;background:var(--dark);color:#fff;text-align:center;padding:52px 34px 0;z-index:3}
.card h2{font-family:"Orbitron",sans-serif;font-weight:700;color:var(--orange);font-size:23px;letter-spacing:1.5px;text-transform:uppercase}
.card .rule{width:30px;height:2px;background:var(--orange);margin:14px auto 18px}
.card h3{font-size:12.5px;font-weight:700;text-transform:uppercase;letter-spacing:.5px;margin-bottom:40px}
.card p{font-size:12.5px;line-height:19px;color:var(--muted)}
.card .more{display:block;margin-top:24px;font-size:12.5px;font-weight:700;color:var(--orange)}
.card.small{padding:34px 22px 0}
.card.small h2{font-size:15px}
.card.small .rule{margin:12px auto 16px}
.frame{position:absolute;border:2px solid var(--orange);z-index:2}

/* recent band */
.recent{position:absolute;left:30px;top:1168px;width:1140px;height:495px}
.section-title{font-family:"Orbitron",sans-serif;font-weight:700;color:var(--orange);font-size:31px;letter-spacing:3px;text-transform:uppercase;text-align:center;position:absolute;left:0;width:100%}
.section-sub{position:absolute;left:0;width:100%;text-align:center;font-size:15px;font-weight:700;text-transform:uppercase}
.recent .section-sub{color:#fff}
.project{position:absolute;top:202px;width:276px}
.project .photo{position:static;height:190px;display:block}
.project span{display:block;text-align:center;margin-top:22px;font-size:12.5px;color:#ddd;text-transform:uppercase;letter-spacing:1px}

/* services */
.services{position:absolute;left:30px;top:1668px;width:1140px;height:1669px;background:var(--panel)}

/* gallery */
.gallery-grid{position:absolute;left:30px;top:3539px;width:1140px;height:369px;display:grid;grid-template-columns:repeat(4,1fr);grid-template-rows:repeat(2,1fr)}
.gallery-grid div{width:100%;height:100%}
.view-all{position:absolute;left:0;width:1200px;top:3938px;text-align:center;color:var(--orange);font-size:13px;font-weight:600}

/* footer */
.site-footer{position:absolute;left:30px;top:3999px;width:1140px;height:381px;background:var(--band);color:#ddd}
.f-col{position:absolute;top:70px}
.f-col h4{font-size:14px;font-weight:700;text-transform:uppercase;letter-spacing:1px;color:#fff;margin-bottom:22px}
.contact-item{display:flex;gap:14px;margin-bottom:14px;padding-bottom:12px;border-bottom:1px solid #575757;width:232px}
.contact-item svg{flex:none;margin-top:2px}
.contact-item b{display:block;color:var(--orange);font-size:12.5px;font-weight:600}
.contact-item small{font-size:11px;color:#aaa}
.links li{list-style:none;font-size:11.5px;color:#bbb;margin-bottom:12px;display:flex;align-items:center;gap:9px}
.links li::before{content:"";width:5px;height:5px;border-radius:50%;background:var(--grey)}
.news p{font-size:11px;line-height:17px;color:#aaa;width:250px;margin-bottom:20px}
.news-form{display:flex;width:262px;height:36px}
.news-form span{flex:1;background:#2a2a2a;font-size:11px;color:#888;padding:10px 12px}
.news-form i{width:36px;background:#2a2a2a;display:flex;align-items:center;justify-content:center;border-left:1px solid #444}
.copyright{position:absolute;left:435px;top:318px;font-size:11px;color:#aaa}
.social{position:absolute;left:905px;top:314px;display:flex;gap:10px}
.social span{width:22px;height:22px;background:#2a2a2a;border-radius:2px}
</style>
</head>
<body>

<header class="site-header">
  <div class="nav-link nav-menu">
    <svg width="12" height="10" viewBox="0 0 12 10"><rect width="12" height="2" fill="#f78f20"/><rect y="4" width="12" height="2" fill="#f78f20"/><rect y="8" width="12" height="2" fill="#f78f20"/></svg>Menu
  </div>
  <div class="brand">
    <span class="brand-mark"></span>
    <span class="brand-name">Cobalt Mesa<br>Lighting and Design</span>
  </div>
  <div class="nav-link nav-follow">
    <svg width="12" height="12" viewBox="0 0 12 12"><circle cx="9.5" cy="2.5" r="2" fill="#f78f20"/><circle cx="2.5" cy="6" r="2" fill="#f78f20"/><circle cx="9.5" cy="9.5" r="2" fill="#f78f20"/><path d="M9.5 2.5L2.5 6L9.5 9.5" stroke="#f78f20" stroke-width="1.2" fill="none"/></svg>Follow
  </div>
</header>

<div class="photo" role="img" aria-label="Lounge interior with warm wall washer lights over a long bench" style="left:30px;top:82px;width:1140px;height:495px;background:radial-gradient(ellipse at 35% 35%,#c9a377 0%,#6e553c 35%,#2d241b 75%,#16110d 100%)"></div>

<!-- welcome -->
<div class="photo" role="img" aria-label="Teacup pendant lamps glowing in a dim room" style="left:173px;top:644px;width:638px;height:456px;background:radial-gradient(circle at 35% 35%,#f3d9a8 0%,#8a6644 30%,#3b2d22 70%,#1f1915 100%)"></div>
<div class="frame" style="left:703px;top:694px;width:331px;height:354px"></div>
<div class="card" style="left:688px;top:661px;width:328px;height:358px">
  <h2>Welcome!</h2>
  <div class="rule"></div>
  <h3 style="margin-bottom:34px">Let us lighten your place!</h3>
  <p>Cobalt Mesa Lighting was established in 1996 and is the leading lighting and controls agency in the region, servicing the Southwest and beyond.</p>
  <span class="more">Know more</span>
</div>

<!-- recently done -->
<section class="recent" role="img" aria-label="Dark backdrop of blurred hanging globe lights" style="background:radial-gradient(circle at 20% 40%,#3a3a3a 0%,#1e1e1e 45%,#121212 100%)">
  <h2 class="section-title" style="top:58px">Recently Done</h2>
  <div class="abs" style="left:555px;top:108px;width:30px;height:2px;background:var(--orange)"></div>
  <p class="section-sub" style="top:122px">We look forward in working with you!</p>
  <div class="project" style="left:140px">
    <div class="photo" role="img" aria-label="Bright conference room with long tables" style="background:linear-gradient(180deg,#e7ecef 0%,#b7bfc4 55%,#3a3f45 100%)"></div>
    <span>Mesa Convention Center</span>
  </div>
  <div class="project" style="left:435px">
    <div class="photo" role="img" aria-label="Hotel restaurant with warm orange lighting" style="background:linear-gradient(160deg,#d78a3e 0%,#8b4520 50%,#3a1b10 100%)"></div>
    <span>Harbor Lane Hotel</span>
  </div>
  <div class="project" style="left:731px">
    <div class="photo" role="img" aria-label="Building facade lit in green and blue at night" style="background:linear-gradient(150deg,#1d3e7a 0%,#2f8a5a 45%,#163020 100%)"></div>
    <span>Norvale Civic Hall</span>
  </div>
</section>

<!-- services -->
<section class="services"></section>

<div class="photo" role="img" aria-label="Commercial lobby with round ceiling cove light and lounge seating" style="left:392px;top:1733px;width:638px;height:457px;background:linear-gradient(170deg,#f4f1ea 0%,#d8cdb8 45%,#8c7658 80%,#4c3c2c 100%)"></div>
<div class="frame" style="left:170px;top:1773px;width:328px;height:363px"></div>
<div class="card" style="left:187px;top:1750px;width:331px;height:355px">
  <h2>Commercial</h2>
  <div class="rule"></div>
  <h3>Lorem ipsum dolor sit amet</h3>
  <p>Lorem ipsum dolor sit amet, consectetur adipiscing elit, sed do eiusmod tempor incididunt ut labore et dolore magna aliqua. Ut enim ad minim veniam quis nostrud.</p>
  <span class="more">Know more</span>
</div>

<div class="photo" role="img" aria-label="Two-storey house lit warmly at dusk under a blue sky" style="left:173px;top:2260px;width:638px;height:457px;background:linear-gradient(180deg,#2f5fb0 0%,#4a7ac8 35%,#c09a62 65%,#3d5a2a 100%)"></div>
<div class="frame" style="left:703px;top:2310px;width:331px;height:357px"></div>
<div class="card" style="left:688px;top:2280px;width:328px;height:349px">
  <h2>Residential</h2>
  <div class="rule"></div>
  <h3>Cobalt Mesa Lighting</h3>
  <p>Ex commodo consequat. Duis aute irure dolor in reprehenderit in voluptate velit esse cillum dolore eu fugiat nulla pariatur. Excepteur sint occaecat cupidatat non proident.</p>
  <span class="more">Know more</span>
</div>

<div class="frame" style="left:196px;top:2787px;width:419px;height:477px"></div>
<div class="photo" role="img" aria-label="Living room with recessed ceiling lights and wall unit" style="left:181px;top:2933px;width:407px;height:307px;z-index:2;background:linear-gradient(175deg,#f2ece2 0%,#c8b9a2 50%,#6b5b4a 100%)"></div>
<div class="card small" style="left:173px;top:2833px;width:269px;height:173px">
  <h2>Lighting Controls</h2>
  <div class="rule"></div>
  <p style="font-size:11.5px;line-height:17px">Ex commodo consequat. Duis aute irure dolor in reprehe</p>
  <span class="more" style="margin-top:12px">Know more</span>
</div>

<div class="frame" style="left:761px;top:2930px;width:258px;height:313px"></div>
<div class="photo" role="img" aria-label="Auditorium with circular skylight and rows of seats" style="left:615px;top:2787px;width:407px;height:325px;background:linear-gradient(180deg,#cfd3d6 0%,#8d9195 40%,#3a3c40 75%,#1e1f22 100%)"></div>
<div class="card small" style="left:785px;top:3039px;width:248px;height:169px">
  <h2>Electrical Materials</h2>
  <div class="rule"></div>
  <p style="font-size:11.5px;line-height:17px">Aspernatur aut odit aut fugit, sed quia consequuntur.</p>
  <span class="more" style="margin-top:12px">Know more</span>
</div>

<!-- gallery -->
<h2 class="section-title" style="top:3390px">Cobalt Mesa Lighting Gallery</h2>
<div class="abs" style="left:585px;top:3440px;width:30px;height:2px;background:var(--orange)"></div>
<p class="section-sub" style="top:3458px;text-transform:none;font-size:16px">Voluptate velit esse cillum</p>
<div class="gallery-grid">
  <div role="img" aria-label="Ceiling with pattern of downlight spots" style="background:linear-gradient(180deg,#f0eee9,#9a8f82)"></div>
  <div role="img" aria-label="Modern villa with garden lights at night" style="background:linear-gradient(180deg,#16305a,#6a5a3a)"></div>
  <div role="img" aria-label="Lobby with coffered ceiling lighting" style="background:linear-gradient(180deg,#cfd8e2,#7c8a98)"></div>
  <div role="img" aria-label="Hall with round ceiling light features" style="background:linear-gradient(180deg,#e6dccb,#8d7558)"></div>
  <div role="img" aria-label="Palm trees uplit by garden lights" style="background:linear-gradient(180deg,#1a1f14,#7a6a32)"></div>
  <div role="img" aria-label="White room with blue ring light" style="background:linear-gradient(180deg,#4c64d8,#e4e8f0)"></div>
  <div role="img" aria-label="Restaurant with amber pendant lights" style="background:linear-gradient(180deg,#3a2414,#c07a30)"></div>
  <div role="img" aria-label="Lounge bar with purple ceiling glow" style="background:linear-gradient(180deg,#5b2c9a,#1e1430)"></div>
</div>
<p class="view-all">View all photos</p>

<!-- footer -->
<footer class="site-footer">
  <div class="f-col" style="left:143px">
    <h4>Contact Information</h4>
    <div class="contact-item">
      <svg width="16" height="16" viewBox="0 0 16 16"><path d="M8 1a5 5 0 0 0-5 5c0 4 5 9 5 9s5-5 5-9a5 5 0 0 0-5-5z" fill="none" stroke="#959595" stroke-width="1.4"/><circle cx="8" cy="6" r="1.8" fill="#959595"/></svg>
      <div><b>Address</b><small>1200 Ridgeway Ave, Mesa Ridge, NM 87000</small></div>
    </div>
    <div class="contact-item">
      <svg width="16" height="16" viewBox="0 0 16 16"><path d="M3 1.5l3 .5 1 3.5-2 1.2a9 9 0 0 0 4.3 4.3l1.2-2 3.5 1 .5 3C12 14 2 8 3 1.5z" fill="none" stroke="#959595" stroke-width="1.4"/></svg>
      <div><b>Phone</b><small>505-555-0175</small></div>
    </div>
    <div class="contact-item">
      <svg width="16" height="16" viewBox="0 0 16 16"><rect x="1" y="3" width="14" height="10" fill="none" stroke="#959595" stroke-width="1.4"/><path d="M1 3l7 6 7-6" fill="none" stroke="#959595" stroke-width="1.4"/></svg>
      <div><b>Email</b><small>hello@cobaltmesalighting.example</small></div>
    </div>
    <div class="contact-item" style="border:0">
      <svg width="16" height="16" viewBox="0 0 16 16"><circle cx="8" cy="8" r="6.5" fill="none" stroke="#959595" stroke-width="1.4"/><path d="M8 4v4l3 2" fill="none" stroke="#959595" stroke-width="1.4"/></svg>
      <div><b>Hours of Operation</b><small>Mon-Fri 8:00 AM to 5:00 PM</small></div>
    </div>
  </div>
  <div class="f-col" style="left:435px">
    <h4>Links</h4>
    <ul class="links">
      <li>Lighting Installation Mesa</li>
      <li>LED Lighting</li>
      <li>Office Lighting</li>
      <li>Lighting Design</li>
      <li>Outdoor Lighting LED</li>
    </ul>
  </div>
  <div class="f-col news" style="left:731px">
    <h4>Newsletter</h4>
    <p>Signup to our newsletter and stay updated with our latest offer and news</p>
    <div class="news-form">
      <span>Enter email id</span>
      <i><svg width="12" height="12" viewBox="0 0 12 12"><path d="M1 6l10-5-3 10-2-4z" fill="#f78f20"/></svg></i>
    </div>
  </div>
  <p class="copyright">Copyright © Cobalt Mesa Lighting 2017</p>
  <div class="social"><span></span><span></span><span></span></div>
</footer>

</body>
</html>
```